Website for a company offering full serivce charging solutions for electric cars

The company "mero-kant" (english: "mero-edge") offering all-in-one-solutions for charging infrastructure for electric mobility.

There are four products:
1- Wallboxes for single-family homes
2- Solutions for property devloper/-management for property parking space
3- All-in-one-charging solution for municipalities/communities
4- Solutions for tourism/hotels/holiday appartments

The Website structure:
1. Main Page
2.1. Product Page Single Homes
2.2. Product Page Property Management / Parking
2.3. Product Page Municipality
2.4. Product Page Tourism
3. Contact Form / Request for information
4. Imprint / Legal

The Website should be built on Wordpress with a powerful possibility to simply add/modify specific landing pages.

We would like you to implement the website later and also maintain it if possible, but we would be able to do minor modifications by ourselfs (for A/B-Testing)

The website should be clear and simple, easy to understand.
Target group is mainly B2C without deeper knowledge of that topic.

It should suggest, that we will provide a very simple way to get the charging infrastructure done.

We need a contact form, maybe we will use Hubspot later.

Attached you will find a draft of the main page and a landing page (for 2.2) - it is just the content, please ignore the design. We would love to let you create a suitable design.
Also you will find some drafts a bit different for the same story.

I added also a few stock photos, but they don't need to be used! If you have better ideas, you are welcome!

Industry/Entity Type

Charging/Electric mobility

Number of Pages Required

2 page

Font styles to use
Sans Serif

Requirements
Must have
• Based on Wordpress, and the designer should be able to implement it on Wordpress on a later step

```html
<!DOCTYPE html>
<html lang="de">
<head>
<meta charset="utf-8">
<title>mero-kant – einfach mehr als laden</title>
<link href="https://fonts.googleapis.com/css2?family=Audiowide&family=Poppins:wght@400;500;600&display=swap" rel="stylesheet">
<style>
:root{
  --bg:#121a2b;
  --bg-deep:#0f1524;
  --pink:#d22eb5;
  --violet:#6a4fd0;
  --white:#ffffff;
  --text:#e9ebf2;
  --head-font:'Audiowide',sans-serif;
  --body-font:'Poppins',sans-serif;
}
*{margin:0;padding:0;box-sizing:border-box}
html,body{width:1200px;height:3250px;overflow:hidden;background:var(--bg)}
body{position:relative;font-family:var(--body-font);color:var(--text)}
.abs{position:absolute}

/* header */
.site-header{position:absolute;left:0;top:0;width:1200px;height:88px;background:var(--bg-deep);border-bottom:3px solid var(--pink)}
.brand{position:absolute;left:104px;top:22px;display:flex;align-items:center;gap:12px}
.brand-dot{width:34px;height:34px;border:3px solid var(--pink);border-radius:50%}
.brand-name{font-size:26px;font-weight:500;color:var(--white);line-height:1}
.brand-tag{font-size:12px;color:var(--white);margin-top:3px;padding-left:16px}
.main-nav{position:absolute;top:34px;left:0;width:1200px;font-size:16px;font-weight:500}
.main-nav a{position:absolute;color:var(--white);text-decoration:none}
.main-nav a.active{color:var(--pink)}

/* hero */
.hero{position:absolute;left:0;top:91px;width:1200px;height:642px;
  background:linear-gradient(100deg,#e0a24a 0%,#c98b3f 25%,#6f5a48 48%,#3a3531 60%,#d9dde2 78%,#aeb6bf 100%)}
.hero-title{position:absolute;left:100px;top:300px;font-family:var(--head-font);font-size:68px;color:var(--white);letter-spacing:1px}
.hero-sub{position:absolute;left:100px;top:388px;font-size:37px;color:var(--white)}
.btn-start{position:absolute;left:102px;top:460px;width:153px;height:42px;border-radius:21px;
  background:linear-gradient(90deg,var(--pink),var(--violet));color:var(--white);font-size:15px;font-weight:600;
  display:flex;align-items:center;justify-content:center}

/* intro */
.section-title{font-family:var(--head-font);color:var(--pink);font-size:38px}
.intro-title{position:absolute;left:0;top:815px;width:1200px;text-align:center}
.intro-lead{position:absolute;left:0;top:888px;width:1200px;text-align:center;font-size:18px;font-weight:500;color:var(--white)}
.intro-text{position:absolute;left:101px;top:925px;width:999px;font-size:15px;line-height:29.5px;text-align:justify;text-align-last:center;color:var(--white)}
.intro-text .hl{color:var(--pink)}
.intro-ask{position:absolute;left:0;top:1140px;width:1200px;text-align:center;font-size:18px;font-weight:600;color:var(--white)}

/* offers */
.offer-photo{position:absolute}
.offer-heading{position:absolute}
.feature-list{position:absolute;list-style:none;font-size:15px;line-height:20.5px;color:var(--white)}
.feature-list li{position:relative;padding-left:18px;margin-bottom:16px}
.feature-list li::before{content:"";position:absolute;left:0;top:6px;width:10px;height:10px;border-radius:50%;border:2px solid var(--pink);box-shadow:inset 0 0 0 2px var(--bg);background:var(--pink)}
.feature-list.gap-lg li{margin-bottom:28px}
.sub-list{position:absolute;list-style:none;font-size:12px;line-height:24px;color:var(--white)}
.sub-list li{padding-left:14px;position:relative}
.sub-list li::before{content:"-";position:absolute;left:0;color:var(--pink)}

/* footer */
.footer-rule{position:absolute;left:0;top:3028px;width:1200px;height:5px;background:linear-gradient(90deg,var(--violet),var(--pink))}
.site-footer{position:absolute;left:0;top:3033px;width:1200px;height:217px;background:var(--bg-deep)}
.social{position:absolute;top:51px;width:48px;height:48px;border-radius:50%;background:linear-gradient(135deg,var(--violet),var(--pink))}
.footer-nav{position:absolute;left:0;top:123px;width:1200px;text-align:center;font-size:16px;color:var(--white)}
.footer-nav span.sep{margin:0 28px}
.copyright{position:absolute;left:0;top:169px;width:1200px;text-align:center;font-size:15px;color:var(--white)}
</style>
</head>
<body>

<header class="site-header">
  <div class="brand">
    <span class="brand-dot"></span>
    <div>
      <div class="brand-name">mero-kant.de</div>
      <div class="brand-tag">einfach mehr als laden</div>
    </div>
  </div>
  <nav class="main-nav">
    <a class="active" style="left:547px">Lösungen</a>
    <a style="left:667px">Unternehmen</a>
    <a style="left:820px">Services</a>
    <a style="left:930px">Karriere</a>
    <a style="left:1037px">Kontakt</a>
  </nav>
</header>

<section class="hero" role="img" aria-label="Foto: Frau mit Smartphone lädt ein weißes Elektroauto bei Sonnenuntergang">
  <h1 class="hero-title">mero kant de</h1>
  <p class="hero-sub">einfach mehr als laden</p>
  <span class="btn-start">GET STARTED</span>
</section>

<h2 class="section-title intro-title">mero-kant ist Ihr Partner</h2>
<p class="intro-lead">wenn das Laden nicht nur einfach, sondern die Umsetzung auch aus einer Hand kommen soll</p>
<p class="intro-text">Wir bieten Lösungen sowohl für <span class="hl">Privatkunden, Geschäftskunden</span> als auch <span class="hl">Kommunen</span> an, die schnell, fair und ohne Eigenleistung zu einer smarten Ladelösung für E-Fahrzeuge kommen möchten. Von der Beratung, über die Installation, Inbetriebnahme bis zur Abrechnung und Wartung bekommen Sie bei mero-kant alles aus einer Hand. Auf Wunsch vermieten wir auch die Ladetechnik und übernehmen im gewerblichen Bereich die direkte Abrechnung mit dem Nutzer. Für Kommunen bieten wir den kostenfreien Full-Service an und beteiligen die Gemeinden an der Nutzung der Infrastruktur.</p>
<p class="intro-ask">Fragen Sie uns nach der auf Ihre individuellen Bedürfnisse zugeschnittenen Lösung:</p>

<!-- Privatkunde -->
<svg class="offer-photo" style="left:62px;top:1252px" width="478" height="478" viewBox="0 0 478 478">
  <defs><linearGradient id="ringA" x1="0" y1="0" x2="0" y2="1"><stop offset="0" stop-color="#6a4fd0"/><stop offset="1" stop-color="#d22eb5"/></linearGradient>
  <radialGradient id="photoA" cx=".6" cy=".45" r=".7"><stop offset="0" stop-color="#3a6df0"/><stop offset=".5" stop-color="#9fb4de"/><stop offset="1" stop-color="#1c2c6a"/></radialGradient></defs>
  <circle cx="239" cy="239" r="236" fill="none" stroke="url(#ringA)" stroke-width="2" stroke-dasharray="7 5"/>
  <circle cx="239" cy="239" r="219" fill="url(#photoA)" role="img" aria-label="Foto: Ladestecker in blau leuchtender Ladebuchse eines Elektroautos"/>
</svg>
<h2 class="section-title offer-heading" style="left:576px;top:1296px">als Privatkunde</h2>
<ul class="feature-list gap-lg" style="left:576px;top:1362px;width:270px">
  <li>Bestandsanalyse mit umfangreicher Beratung über die Möglichkeiten der Umsetzung</li>
  <li>Planung und Projektsteuerung inkl. sämtlicher behördlicher Genehmigungsverfahren und Beantragung von Fördermitteln</li>
  <li>Fachgerechte Installation und Inbetriebnahme</li>
  <li>Regelmäßige Wartung gemäß Vorschrif</li>
</ul>
<ul class="feature-list" style="left:857px;top:1362px;width:275px">
  <li>Reparatur und Kundenservice</li>
  <li>Direkte Abrechnung mit dem Nutzer</li>
  <li>Beteiligung der Gemeinde am Umsatz</li>
  <li>Möglichkeit der Integration von Bonusprogrammen, mit denen der lokale Einzelhandel beworben wird</li>
</ul>

<!-- Geschäftskunde 1 -->
<h2 class="section-title offer-heading" style="left:63px;top:1845px">als Geschäftskunde</h2>
<ul class="feature-list gap-lg" style="left:63px;top:1912px;width:265px">
  <li>Planung und Projektierung des Installationsaufwands inkl. Materialverbrauch</li>
  <li>Planung und Projektierung des Installationsaufwands inkl. Materialverbrauch</li>
  <li style="margin-bottom:12px">Leasing oder Kauf der Hardware</li>
  <li>Normgerechte Installation der Ladeinfrastruktur inkl. Durchbruch-, Brandschutz- und Erdarbeiten</li>
  <li>Bei Bestandsbauten Integration der Ladeinfrastruktur in die Gebäudesystemtechnik und ggf. Anpassung des Netzanschlusses</li>
</ul>
<ul class="sub-list" style="left:338px;top:1908px">
  <li>Haus- und Immobilienverwaltungen</li>
  <li>Dienstleistungs- und Handelsunternehmen</li>
  <li>Hotel und Beherbergungsbetriebe</li>
  <li>Parkraum- und Parkhausbetreiber</li>
  <li>Tourismus, Sport- und Freizeiteinrichtungen</li>
</ul>
<ul class="feature-list" style="left:344px;top:2040px;width:270px">
  <li>Inbetriebnahme der Anlage inkl. Prüf- und Messprotokollen</li>
  <li>Wiederkehrende technische Prüfung der Anlage nach DGUV 3</li>
  <li>Austausch und Reparatur Service</li>
  <li>Unterstützung bei der mtl. Nutzungsabrechnung und Einbindung in Ihre vorhandene Abrechnungssysteme</li>
  <li>ODER direkte Abrechnung mit den Nutzern</li>
</ul>
<svg class="offer-photo" style="left:663px;top:1850px" width="478" height="478" viewBox="0 0 478 478">
  <defs><linearGradient id="ringB" x1="0" y1="0" x2="0" y2="1"><stop offset="0" stop-color="#6a4fd0"/><stop offset="1" stop-color="#d22eb5"/></linearGradient>
  <radialGradient id="photoB" cx=".35" cy=".55" r=".7"><stop offset="0" stop-color="#9aa3c2"/><stop offset=".5" stop-color="#3d4670"/><stop offset="1" stop-color="#1a2138"/></radialGradient></defs>
  <circle cx="239" cy="239" r="236" fill="none" stroke="url(#ringB)" stroke-width="2" stroke-dasharray="7 5"/>
  <circle cx="239" cy="239" r="219" fill="url(#photoB)" role="img" aria-label="Foto: blauer Ladestecker an einer Ladesäule im Parkhaus"/>
</svg>

<!-- Geschäftskunde 2 -->
<svg class="offer-photo" style="left:62px;top:2440px" width="478" height="478" viewBox="0 0 478 478">
  <defs><linearGradient id="ringC" x1="0" y1="0" x2="0" y2="1"><stop offset="0" stop-color="#6a4fd0"/><stop offset="1" stop-color="#d22eb5"/></linearGradient>
  <radialGradient id="photoC" cx=".4" cy=".55" r=".7"><stop offset="0" stop-color="#c7d3e6"/><stop offset=".55" stop-color="#8ea5c6"/><stop offset="1" stop-color="#e4ebf4"/></radialGradient></defs>
  <circle cx="239" cy="239" r="236" fill="none" stroke="url(#ringC)" stroke-width="2" stroke-dasharray="7 5"/>
  <circle cx="239" cy="239" r="219" fill="url(#photoC)" role="img" aria-label="Foto: Ladestecker in einer Ladebuchse, hell und kühl ausgeleuchtet"/>
</svg>
<h2 class="section-title offer-heading" style="left:576px;top:2436px">als Geschäftskunde</h2>
<ul class="feature-list gap-lg" style="left:576px;top:2506px;width:270px">
  <li>Konzeptionierung möglicher Ladeinfrastrukturen innerhalb Ihrer Gemeinde</li>
  <li>Planung und Projektierung des Installationsaufwands inkl. Materialverbrauch</li>
  <li style="margin-bottom:12px">Leasing oder Kauf der Hardware</li>
  <li>Normgerechte Installation der Ladeinfrastruktur inkl. Durchbruch-, Brandschutz- und Erdarbeiten</li>
  <li>Bei Bestandsbauten Integration der Ladeinfrastruktur in die Gebäudesystemtechnik und ggf. Anpassung des Netzanschlusses</li>
</ul>
<ul class="feature-list" style="left:857px;top:2509px;width:275px">
  <li>Inbetriebnahme der Anlage inkl. Prüf- und Messprotokollen</li>
  <li>Wiederkehrende technische Prüfung der Anlage nach DGUV 3</li>
  <li>Austausch und Reparatur Service</li>
  <li>Unterstützung bei der mtl. Nutzungsabrechnung und Einbindung in Ihre vorhandene Abrechnungssysteme</li>
  <li>ODER direkte Abrechnung mit den Nutzern</li>
</ul>

<div class="footer-rule"></div>
<footer class="site-footer">
  <span class="social" style="left:513px" aria-label="Video-Kanal"></span>
  <span class="social" style="left:576px" aria-label="Soziales Netzwerk"></span>
  <span class="social" style="left:639px" aria-label="Foto-Netzwerk"></span>
  <nav class="footer-nav">AGB Datenschutzerklarung<span class="sep">|</span>Impressum<span class="sep">|</span>Kontakt<span class="sep">|</span>Karriere<span class="sep">|</span>FAQ</nav>
  <p class="copyright">©mero-kant GmbH</p>
</footer>

</body>
</html>
```